Up and coming mattress store needs a better website design

We are a family owned mattress store called Quillby Sleep and we are in need of a better looking website. We have started advertising online and our current website quillbysleepshop.com is really bad. We are looking for at lest 4 pages including: welcome page, about us page, our mattresses page, and contact us page. Here is a wire frame of something I was thinking of https://sketchplan.io/4rk2TQ it doesn't have to be like this it is just an idea. Some must haves are: Name, Logo, at lest 3 spots for links for financing, a bigger spot for special offers, maybe the number and address for the store at the very bottom. You can submit a one page welcome design to start with and if I like it we can move on from there. Thank you for your time!

Target Market(s)

20 to 40 year olds who want to buy mattresses

Industry/Entity Type

Store

Requirements
Must have
• name, logo, 3 spots for links for our no credit check financing companies
Nice to have
• All stores addresses and numbers at the bottom: Main Store 2718 Marlowe Hwy South Houston 77942 (346)-555-0148 Smaller Store 4420 Hwy 9 Alvin Tx 77836 (281)-555-0193

```html
<!DOCTYPE html>
<html lang="en">
<head>
<meta charset="utf-8">
<title>Quillby Sleep – Family Owned Mattress Store</title>
<link href="https://fonts.googleapis.com/css2?family=Comfortaa:wght@400;700&family=Lato:wght@400;700&display=swap" rel="stylesheet">
<style>
:root{
  --red:#c8141b;
  --red-dark:#8f0a0f;
  --ink:#222;
  --text:#3a3a3a;
  --topbar:#2b2320;
  --panel:#3a3a3a;
  --strip:#1d1d1d;
  --footer:#333;
  --footer-dark:#232323;
  --white:#fff;
}
*{box-sizing:border-box;margin:0;padding:0}
html,body{width:1037px;height:1200px;overflow:hidden}
body{font-family:'Lato',sans-serif;color:var(--text);background:var(--white);position:relative}
.abs{position:absolute}
.topbar{left:0;top:0;width:1037px;height:34px;background:linear-gradient(90deg,#3b2a20,#2b2320 60%,#3a2a20)}
.topbar .contact-line{right:84px;top:8px;display:flex;gap:22px;color:#fff;font-size:13px;align-items:center}
.topbar .contact-line span{display:flex;align-items:center;gap:8px}
.topbar .phone{font-weight:700;font-size:14px}
.header{left:0;top:34px;width:1037px;height:60px;background:var(--white)}
.brand{left:85px;top:12px;display:flex;align-items:center;gap:8px}
.brand-mark{width:24px;height:24px;border-radius:50%;background:var(--red)}
.brand-name{font-family:'Comfortaa',sans-serif;font-weight:700;font-size:22px;color:var(--red)}
.tagline{left:283px;top:12px;font-family:'Comfortaa',sans-serif;font-weight:700;font-size:12.5px;line-height:17px;color:var(--ink)}
.nav{left:494px;top:0;height:60px;display:flex}
.nav a{display:flex;align-items:center;justify-content:center;height:60px;font-size:13.5px;color:var(--ink);text-decoration:none;border-right:1px solid #e6e6e6;letter-spacing:.2px}
.nav a.active{border-bottom:3px solid var(--red);box-shadow:inset 0 3px 0 #eee}
.hero{left:0;top:94px;width:1037px;height:388px;background:radial-gradient(ellipse at 55% 55%,#a08c7a 0%,#6d4a33 35%,#3e2618 70%,#24150d 100%)}
.hero-caption{left:0;top:254px;width:1037px;text-align:center;color:#fff}
.hero-band{left:230px;top:254px;width:580px;height:134px;background:linear-gradient(180deg,rgba(40,30,25,.45),rgba(20,14,10,.6))}
.hero h1{font-family:'Comfortaa',sans-serif;font-weight:700;font-size:23px;margin-top:12px;text-shadow:0 1px 3px rgba(0,0,0,.6)}
.hero p{font-size:13.5px;margin-top:10px;text-shadow:0 1px 2px rgba(0,0,0,.7)}
.btn{display:inline-block;background:var(--red);color:#fff;font-size:14px;width:130px;height:37px;line-height:37px;text-align:center;text-decoration:none;text-shadow:0 1px 1px rgba(0,0,0,.3)}
.hero .btn{margin-top:12px}
.dots{left:0;top:476px;width:1037px;display:flex;justify-content:center;gap:9px}
.dots i{width:7px;height:7px;border-radius:50%;background:#bbb;display:block}
.dots i.on{background:#fff}
.features{left:0;top:482px;width:1037px;height:320px;background:var(--panel)}
.card{top:37px;width:272px;height:244px;background:var(--white);padding:7px}
.card-media{width:258px;height:111px;border:1px solid #ccc}
.card h2{font-family:'Comfortaa',sans-serif;font-weight:400;font-size:18.5px;color:var(--red-dark);margin:8px 0 0 14px}
.card p{font-size:11.5px;line-height:15.5px;color:var(--text);margin:5px 12px 0 14px}
.card .more{display:block;font-size:11px;font-weight:700;color:var(--red-dark);margin:6px 0 0 14px;text-decoration:none}
.stores{display:flex;margin:6px 0 0 20px}
.store{font-size:11.5px;line-height:14px;color:var(--text);display:flex;gap:8px}
.store b{font-weight:700;color:var(--ink)}
.store-col{width:125px}
.store-col+.store-col{border-left:1px solid #bbb;padding-left:10px}
.store-phone{margin-top:12px;display:flex;gap:8px;font-size:11.5px}
.card .mail{text-align:center;font-size:11.5px;margin-top:7px;display:flex;justify-content:center;gap:8px;align-items:center}
.divider{left:0;top:802px;width:1037px;height:1px;background:#666}
.divider-dot{left:514px;top:798px;width:8px;height:8px;border-radius:50%;background:#777}
.finance{left:0;top:803px;width:1037px;height:164px;background:repeating-linear-gradient(45deg,#1b1b1b 0 2px,#242424 2px 4px)}
.finance a{top:36px;width:259px;height:90px;background:var(--red-dark);display:flex;align-items:center;justify-content:center;color:#fff;text-decoration:none;font-family:'Lato',sans-serif;font-weight:700;font-size:20px;box-shadow:0 0 12px rgba(0,0,0,.7)}
.offer{left:0;top:967px;width:1037px;height:152px;background:var(--white);text-align:center}
.offer h2{font-family:'Comfortaa',sans-serif;font-weight:400;font-size:23px;color:var(--ink);margin-top:26px}
.offer h2 strong{color:var(--red);font-weight:700}
.offer p{font-size:13px;color:var(--ink);margin-top:8px}
.offer .btn{margin-top:12px}
.footer-nav{left:0;top:1119px;width:1037px;height:46px;background:var(--footer);display:flex;justify-content:center;align-items:center}
.footer-nav a{color:#ddd;font-size:11.5px;text-decoration:none;padding:0 27px;border-left:1px solid #666;line-height:12px}
.footer-nav a:first-child{border-left:0;color:#fff}
.copyright{left:0;top:1165px;width:1037px;height:35px;background:var(--footer-dark);color:#ccc;font-size:11.5px;text-align:center;line-height:35px}
</style>
</head>
<body>

<div class="abs topbar">
  <div class="abs contact-line">
    <span><svg width="16" height="14" viewBox="0 0 16 14"><path d="M0 6 L16 0 L11 14 L8 8 Z" fill="#e3262d"/></svg>quillbysleepstore@quillbysleepshop.com</span>
    <span class="phone"><svg width="15" height="15" viewBox="0 0 24 24"><path d="M6.6 10.8a15 15 0 006.6 6.6l2.2-2.2c.3-.3.7-.4 1-.2 1.1.4 2.3.6 3.6.6.6 0 1 .4 1 1V20c0 .6-.4 1-1 1A17 17 0 013 4c0-.6.4-1 1-1h3.5c.6 0 1 .4 1 1 0 1.3.2 2.5.6 3.6.1.3 0 .7-.2 1z" fill="#e3262d"/></svg>(346) 555 0148</span>
  </div>
</div>

<header class="abs header">
  <div class="abs brand"><span class="brand-mark"></span><span class="brand-name">Quillby Sleep</span></div>
  <div class="abs tagline">We are a family owned<br>&amp; operated mattress store</div>
  <nav class="abs nav">
    <a class="active" href="#" style="width:86px">HOME</a>
    <a href="#" style="width:111px">ABOUT US</a>
    <a href="#" style="width:157px">OUR MATTRESSES</a>
    <a href="#" style="width:103px;align-items:flex-start;padding-top:20px">CONTACT US</a>
  </nav>
</header>

<section class="abs hero" role="img" aria-label="Photo of a plush mattress on a bed in a wood-panelled bedroom with lamps and pillows"></section>
<div class="abs hero-band"></div>
<div class="abs hero-caption hero">
  <h1>Brand Bed 80% Off</h1>
  <p>Adjustable Beds Avalible Now! 40 Dollars Down No Credit Check Financing!</p>
  <a class="btn" href="#">BUY NOW</a>
</div>
<div class="abs dots"><i></i><i class="on"></i><i></i><i></i></div>

<section class="abs features">
  <article class="abs card" style="left:85px">
    <div class="card-media" role="img" aria-label="Photo of a bedroom with a grey patterned duvet and blue wall" style="background:linear-gradient(135deg,#8fa6b6,#c9c3bb 45%,#a49b92)"></div>
    <h2>About Quillby Sleep</h2>
    <p>Quillby Sleep is Family-Owned and Operated Business. Our Houston and Alvin Mattress Stores are Conveniently Located. We Carry Name Brand Mattresses by Popular Brands.</p>
    <a class="more" href="#">Read More &gt;&gt;</a>
  </article>
  <article class="abs card" style="left:382px">
    <div class="card-media" role="img" aria-label="Photo of a white pillow-top mattress with grey pillows" style="background:linear-gradient(180deg,#3a3836,#9a9690 50%,#2a2826)"></div>
    <h2>Our Mattress</h2>
    <p>Only The Best Quality Mattress Here. At the Best Prices In The Houston Area! Gel Foam, Memory Foam, Latex Foam, Soft Firm, Ultra Firm we got it all for all price ranges!</p>
    <a class="more" href="#">Read More &gt;&gt;</a>
  </article>
  <article class="abs card" style="left:679px">
    <div class="card-media" role="img" aria-label="Street map showing the store location" style="background:linear-gradient(135deg,#ecebe6,#dedcd4)"></div>
    <h2>Contact Us</h2>
    <div class="stores">
      <div class="store-col">
        <div class="store"><svg width="8" height="11" viewBox="0 0 8 11"><path d="M4 0a4 4 0 014 4c0 3-4 7-4 7S0 7 0 4a4 4 0 014-4z" fill="#b0141a"/><circle cx="4" cy="4" r="1.5" fill="#fff"/></svg><div><b>Main Store</b> :2718 Marlowe Hwy South Houston 77942</div></div>
        <div class="store-phone"><svg width="11" height="11" viewBox="0 0 24 24"><path d="M6.6 10.8a15 15 0 006.6 6.6l2.2-2.2c.3-.3.7-.4 1-.2 1.1.4 2.3.6 3.6.6.6 0 1 .4 1 1V20c0 .6-.4 1-1 1A17 17 0 013 4c0-.6.4-1 1-1h3.5c.6 0 1 .4 1 1 0 1.3.2 2.5.6 3.6.1.3 0 .7-.2 1z" fill="#b0141a"/></svg>(346)-555-0148</div>
      </div>
      <div class="store-col">
        <div class="store"><svg width="8" height="11" viewBox="0 0 8 11"><path d="M4 0a4 4 0 014 4c0 3-4 7-4 7S0 7 0 4a4 4 0 014-4z" fill="#b0141a"/><circle cx="4" cy="4" r="1.5" fill="#fff"/></svg><div><b>Smaller Store</b>:<br>4420 Hwy 9<br>Alvin Tx 77836</div></div>
        <div class="store-phone"><svg width="11" height="11" viewBox="0 0 24 24"><path d="M6.6 10.8a15 15 0 006.6 6.6l2.2-2.2c.3-.3.7-.4 1-.2 1.1.4 2.3.6 3.6.6.6 0 1 .4 1 1V20c0 .6-.4 1-1 1A17 17 0 013 4c0-.6.4-1 1-1h3.5c.6 0 1 .4 1 1 0 1.3.2 2.5.6 3.6.1.3 0 .7-.2 1z" fill="#b0141a"/></svg>(281)-555-0193</div>
      </div>
    </div>
    <div class="mail"><svg width="11" height="10" viewBox="0 0 16 14"><path d="M0 6 L16 0 L11 14 L8 8 Z" fill="#b0141a"/></svg>quillbysleepstore@quillbysleepshop.com</div>
  </article>
</section>

<div class="abs divider"></div>
<div class="abs divider-dot"></div>

<section class="abs finance">
  <a class="abs" href="#" style="left:86px">Brightline Lease</a>
  <a class="abs" href="#" style="left:389px">Harborway Credit</a>
  <a class="abs" href="#" style="left:692px">Keystone Pay</a>
</section>

<section class="abs offer">
  <h2>Name Brand Bed <strong>80%</strong> Off</h2>
  <p>We use brightline lease, harborway credit, keystone pay, it needs to say 40 dollars down no credit check 90 days same as cash.</p>
  <a class="btn" href="#">BUY NOW</a>
</section>

<nav class="abs footer-nav">
  <a href="#">Home</a><a href="#">About Us</a><a href="#">Our Mattresses</a><a href="#">Contact Us</a>
</nav>
<div class="abs copyright">Copyright © 2016 - Quillby Sleep Store &nbsp;|&nbsp; All Rights Reserved</div>

</body>
</html>
```